I am looking for a web design that includes space for a blog, archive and an
“ about me” section. It should be capable of being updated in the future should I decide to build the site. I like edgy, creative, friendly and inviting to go with my logo style.
The Pantry Compass is an approach to breaking down and rebuilding or just tweaking what needs to be done to reach nutritional fitness. That is the actual workout part....journaling through something I call reflective nutrition. By doing this one can actually see what they are doing well and where they may need to improve. It involves goal setting and analyzing one's relationship with food. the workout is more mental in this approach. Physical activity is definitely a part of a strong nutritional foundation, but here I am focusing on the work that goes into creating a positive nutritionally fit person.

1. Blog Section: this will be the foundation of the website. I will write weekly blogs explaining and encouraging readers to use reflective nutrition approach to discover and explore their relationship with food and create healthy nutritional habits, breaking those that have been detrimental thus far. Journaling and realistic goal setting is the key to this approach.

2. Archive: this is the section to store old blogs by date with ability to retrieve and read again. Readers should gave access to this section.

3. About Me: I am a clinical nutritionist with a Bachelors of Science and Masters of Science in Nutrition. I have over 30 years experience working with both inpatient and outpatient populations covering a myriad of conditions requiring nutritional intervention. I am passionate about my field and my goal is to help others achieve their optimal nutritional health. I will share my personal struggle with attaining nutritional fitness. I have the
unique perspective of being both a nutrition professional and patient.
Please note that my blog name is not the name under which I am registered with the Bureau For Dietary Licensing (BDL).Contact me privately if you require more information.
Thank you for stopping by and I hope you will come back.
Peace,
M. Harlow
4. Contact Me: This section will only contain my email address for comments and suggestions Thepantrycompass@mailvento.net
Updates

Hey guys! I am very new to this process and I apologize for not having much detail. I think I added more that may give you a clearer understanding of my project. I know I said that I didn't plan on using illustrations but I am getting a better picture of what you do. Please use all your creative tools and talents and imaginations! But read my description of what the actual pantry compass is. It is more of a mental not physical workout. I will respond to your questions and suggestions. I welcome them. Have fun with this!!! I look forward to seeing your work. . Peace, Mara

Target Market(s)

Anyone interested in a realistic approach to reaching nutrition goals.

Industry/Entity Type

Nutrition

Coding

Coded - Design and coding required

Number of Pages Required

3 page

Colors
fbee3d
ffc214

Requirements
Must have
• An automatic sign-off signature at the end of each blog, preferably in the same font as my logo name. Signature will read:
Peace,
M.
My blog name is M, Harlow
Complementary color scheme to the logo but not white, if at all possible. I don't plan on using illustrations so I am relying on the web design to draw people in. It cannot be dull or bland but still professional.
It must be inviting and personable, not intimidating
I may want to update and add on later. Site should be capable of doing
that....should be buildable.
I love the font that was used in the name of my logo and would like to stay consistant with that, if possible.
Nice to have
• A way to monitor people who visit and return.
Maybe a counter to see how many people have visited
Would it be possible to prominently display my logo on the first page with my contact information and have that open directly to my blog page? Also, would the block page have to be a white background? I prefer it to be a color if that is complementary to the logo olor scheme
Should not have
• Please no illustrations of a gym.
This isn’t a blog about physical fitness. It is a blog requiring people to think about what they consume on a daily basis, breaking bad eating habits and creating positive, healthy ones.
I tried to get pictures and illustrations to use but due to licensure restrictions, I was unable at this time. Although your designs are brilliant, I may not be able to supply appropriate illustrations to do your designs justice.

```html
<!DOCTYPE html>
<html lang="en">
<head>
<meta charset="utf-8">
<title>The Pantry Compass</title>
<link href="https://fonts.googleapis.com/css2?family=Caveat+Brush&family=Mulish:wght@400;600;700&display=swap" rel="stylesheet">
<style>
:root{
  --yellow:#d6b300;
  --yellow-soft:#e4c31a;
  --ink:#1e2029;
  --panel:#272a35;
  --card:#373a44;
  --footer:#1c1e26;
  --text-muted:#9a9ca6;
  --white:#ffffff;
  --hand:'Caveat Brush',cursive;
  --body:'Mulish',sans-serif;
}
*{margin:0;padding:0;box-sizing:border-box}
html,body{width:1200px;height:4641px;overflow:hidden;background:var(--ink);font-family:var(--body);color:var(--white)}
.page{position:relative;width:1200px;height:4641px}
section,header,footer{position:absolute;left:0;width:1200px}
.abs{position:absolute}
.hand{font-family:var(--hand);font-weight:400}
.accent{color:var(--yellow)}
.btn-solid{position:absolute;background:var(--yellow);color:var(--white);border-radius:30px;font-family:var(--hand);display:flex;align-items:center;justify-content:center;font-size:24px}
.btn-outline{position:absolute;border:2px solid var(--white);color:var(--white);border-radius:30px;font-family:var(--hand);display:flex;align-items:center;justify-content:center;font-size:24px;width:148px;height:54px}

/* hero */
.hero{top:0;height:856px}
.hero-photo{position:absolute;inset:0;background:linear-gradient(100deg,#b99a74 0%,#d8c8ab 30%,#9a8a63 55%,#5d5a36 80%,#3f4a2b 100%)}
.brand{position:absolute;left:108px;top:70px;display:flex;align-items:center;gap:14px}
.brand-dot{width:52px;height:52px;border-radius:50%;background:var(--yellow)}
.brand-name{font-family:var(--hand);font-size:40px;color:var(--yellow);line-height:1}
.nav{position:absolute;top:44px;font-family:var(--hand);font-size:22px}
.hero-title{position:absolute;left:600px;top:286px;width:560px;text-align:center;font-family:var(--hand);font-size:72px;color:var(--yellow)}
.hero-sub{position:absolute;left:610px;top:386px;width:540px;text-align:center;font-family:var(--hand);font-size:25px;line-height:38px}

/* welcome */
.welcome{top:856px;height:632px;background:var(--ink)}
.welcome-mark{position:absolute;left:207px;top:180px;width:300px;display:flex;align-items:center;gap:14px}
.welcome-mark .brand-dot{width:70px;height:70px;flex:none}
.welcome-mark .brand-name{font-size:44px}
.welcome-kicker{position:absolute;left:555px;top:92px;font-family:var(--hand);font-size:44px}
.welcome-title{position:absolute;left:555px;top:148px;font-family:var(--hand);font-size:60px;color:var(--yellow)}
.welcome-copy{position:absolute;left:564px;top:234px;width:472px;font-size:13.5px;line-height:26.5px;color:var(--text-muted);text-align:justify}

/* blog */
.blog{top:1488px;height:878px;background:var(--panel)}
.section-title{position:absolute;left:0;width:1200px;text-align:center;font-family:var(--hand);font-size:64px}
.col-rule{position:absolute;left:600px;top:160px;width:1px;height:650px;background:#3a3d49}
.post{position:absolute;width:452px}
.post h3{font-family:var(--hand);font-weight:400;font-size:23px}
.post .meta{margin-top:18px;font-family:var(--hand);font-size:16px;color:var(--yellow);padding-bottom:10px;border-bottom:1px dashed var(--yellow)}
.post .meta span{margin:0 14px}
.post p{margin-top:22px;font-size:13.5px;line-height:25.5px;color:#c8cad2;text-align:justify}
.post .btn-outline{position:relative;margin-top:22px}

/* about */
.about{top:2366px;height:679px}
.about-photo{position:absolute;inset:0;background:linear-gradient(90deg,#1f1b1a 0%,#4a3a30 35%,#8a6a4a 55%,#6a5040 75%,#3a2e2a 100%)}
.about-title{position:absolute;left:661px;top:142px;font-family:var(--hand);font-size:64px}
.about-copy{position:absolute;left:661px;top:234px;width:424px;font-size:13.5px;line-height:25.8px;color:#e6dccf;text-align:justify}

/* archive */
.archive{top:3045px;height:751px;background:var(--panel)}
.arch-card{position:absolute;width:473px;height:227px;background:var(--card)}
.arch-date{position:absolute;left:20px;top:36px;width:134px;height:134px;border-radius:50%;background:var(--yellow);text-align:center;font-family:var(--hand);line-height:1}
.arch-date b{display:block;font-weight:400;font-size:64px;margin-top:18px}
.arch-date i{font-style:normal;font-size:30px}
.arch-body{position:absolute;left:183px;top:28px;width:270px}
.arch-body h4{font-family:var(--hand);font-weight:400;font-size:20px;line-height:31px;color:var(--yellow)}
.arch-body p{margin-top:10px;font-size:13px;line-height:27px;color:#d0d2d8}
.arch-body a{display:inline-flex;align-items:center;gap:8px;margin-top:12px;font-family:var(--hand);font-size:18px;color:var(--yellow);text-decoration:none}

/* call */
.call{top:3796px;height:465px;background:radial-gradient(circle at 50% 40%,#33332f,#232322)}
.call-kicker{position:absolute;left:0;width:1200px;top:98px;text-align:center;font-family:var(--hand);font-size:32px}
.call-phone{position:absolute;left:0;width:1200px;top:136px;text-align:center;font-family:var(--hand);font-size:64px;color:var(--yellow)}
.call-copy{position:absolute;left:240px;width:720px;top:230px;text-align:center;font-size:13px;line-height:26px;color:#d8d8d8}

/* footer */
.site-footer{top:4261px;height:380px;background:var(--footer)}
.foot-brand{position:absolute;left:207px;top:90px;display:flex;flex-direction:column;align-items:center;gap:12px;width:180px}
.foot-brand .brand-dot{width:64px;height:64px}
.foot-brand .brand-name{font-size:34px;text-align:center}
.foot-head{position:absolute;top:70px;font-size:19px;font-weight:600}
.foot-links{position:absolute;left:479px;top:112px;list-style:none;font-size:11px;line-height:21.6px}
.contact-row,.follow-row{position:absolute;display:flex;align-items:flex-start;gap:14px;font-size:11.5px;line-height:16px}
.ico{width:26px;height:26px;border-radius:50%;background:var(--white);flex:none;display:flex;align-items:center;justify-content:center}
.foot-rule{position:absolute;left:112px;top:303px;width:976px;height:1px;background:#34363f}
.copyright{position:absolute;left:0;width:1200px;top:335px;text-align:center;font-size:11.5px}
</style>
</head>
<body>
<div class="page">

<header class="hero">
  <div class="hero-photo" role="img" aria-label="Photo of a smiling woman eating a fresh salad at a kitchen table with vegetables and juices"></div>
  <div class="brand"><span class="brand-dot"></span><span class="brand-name">The Pantry Compass</span></div>
  <nav>
    <span class="nav accent" style="left:564px">Home</span>
    <span class="nav" style="left:663px">Blog</span>
    <span class="nav" style="left:753px">Archive</span>
    <span class="nav" style="left:876px">About Me</span>
    <span class="nav" style="left:1005px">Contact Me</span>
  </nav>
  <h1 class="hero-title">The Pantry Compass</h1>
  <p class="hero-sub">It is a long established fact that a reader will be distracted by the a page when looking at its layout.</p>
</header>

<section class="welcome">
  <div class="welcome-mark"><span class="brand-dot"></span><span class="brand-name">The Pantry Compass</span></div>
  <div class="welcome-kicker">Welcome To</div>
  <h2 class="welcome-title">The Pantry Compass</h2>
  <p class="welcome-copy">It is a long established fact that a reader will be distracted by the readable content of a page when looking at its layout. The point of using Lorem Ipsum is that it has a more-or-less normal distribution of letters, as opposed to using 'Content here, content here', making it look like readable English. Many desktop publishing packages and web page editors now use Lorem Ipsum as their default model text, and a eiusmod tempor incididunt ut labore et dolore magna aliqua.</p>
  <div class="btn-solid" style="left:568px;top:452px;width:176px;height:56px">Read More</div>
</section>

<section class="blog">
  <h2 class="section-title" style="top:38px">Latest <span class="accent">Blog</span></h2>
  <div class="col-rule"></div>
  <article class="post" style="left:112px;top:168px">
    <h3>At vero eos et accusamus et iusto odio dignissimos ducimus</h3>
    <div class="meta">Feb 21,2021<span>|</span>by Dummy Name<span>|</span>2 comments</div>
    <p>Lorem ipsum dolor sit amet, consectetur adipiscing elit, sed do eiu smod tempor incididunt ut labore et dolore magna aliqua. Ut enim ad minim veniam, quis nostrud exercitation ullamco laboris nisi ut aliquip ex ea commodo consequat.</p>
    <div class="btn-outline">Read More</div>
  </article>
  <article class="post" style="left:636px;top:168px">
    <h3>At vero eos et accusamus et iusto odio dignissimos ducimus</h3>
    <div class="meta">Feb 21,2021<span>|</span>by Dummy Name<span>|</span>2 comments</div>
    <p>Lorem ipsum dolor sit amet, consectetur adipiscing elit, sed do eiu smod tempor incididunt ut labore et dolore magna aliqua. Ut enim ad minim veniam, quis nostrud exercitation ullamco laboris nisi ut aliquip ex ea commodo consequat.</p>
    <div class="btn-outline">Read More</div>
  </article>
  <article class="post" style="left:112px;top:525px">
    <h3>At vero eos et accusamus et iusto odio dignissimos ducimus</h3>
    <div class="meta">Feb 21,2021<span>|</span>by Dummy Name<span>|</span>2 comments</div>
    <p>Lorem ipsum dolor sit amet, consectetur adipiscing elit, sed do eiu smod tempor incididunt ut labore et dolore magna aliqua. Ut enim ad minim veniam, quis nostrud exercitation ullamco laboris nisi ut aliquip ex ea commodo consequat.</p>
    <div class="btn-outline">Read More</div>
  </article>
  <article class="post" style="left:636px;top:525px">
    <h3>At vero eos et accusamus et iusto odio dignissimos ducimus</h3>
    <div class="meta">Feb 21,2021<span>|</span>by Dummy Name<span>|</span>2 comments</div>
    <p>Lorem ipsum dolor sit amet, consectetur adipiscing elit, sed do eiu smod tempor incididunt ut labore et dolore magna aliqua. Ut enim ad minim veniam, quis nostrud exercitation ullamco laboris nisi ut aliquip ex ea commodo consequat.</p>
    <div class="btn-outline">Read More</div>
  </article>
</section>

<section class="about">
  <div class="about-photo" role="img" aria-label="Silhouette of a woman meditating outdoors at sunset"></div>
  <h2 class="about-title">About <span class="accent">Me</span></h2>
  <p class="about-copy">It is a long established fact that a reader will be distracted by the readable content of a page when looking at its layout. The point of using Lorem Ipsum is that it has a more-or-less normal distribution of letters, as opposed to using 'Content here, content here', making it look like readable English. Many desktop publishing packages and web page editors now use Lorem Ipsum as their default model text, and a search for 'lorem ipsum' will uncover many web sites still in their infancy.</p>
  <div class="btn-solid" style="left:663px;top:508px;width:173px;height:57px">Read More</div>
</section>

<section class="archive">
  <h2 class="section-title" style="top:42px">Our <span class="accent">Archive</span></h2>
  <div class="arch-card" style="left:112px;top:169px">
    <div class="arch-date"><b>21</b><i>Feb</i></div>
    <div class="arch-body"><h4>At vero eos et accusamus et iusto odio issimos ducimus qui</h4><p>It is a long established fact tha a rea will be distracted readable</p><a>Read More <svg width="14" height="14" viewBox="0 0 14 14"><circle cx="7" cy="7" r="6" fill="none" stroke="currentColor" stroke-width="1.5"/><path d="M5 4.5 8 7 5 9.5" fill="none" stroke="currentColor" stroke-width="1.5"/></svg></a></div>
  </div>
  <div class="arch-card" style="left:614px;top:169px">
    <div class="arch-date"><b>21</b><i>Feb</i></div>
    <div class="arch-body"><h4>At vero eos et accusamus et iusto odio issimos ducimus qui</h4><p>It is a long established fact tha a rea will be distracted readable</p><a>Read More <svg width="14" height="14" viewBox="0 0 14 14"><circle cx="7" cy="7" r="6" fill="none" stroke="currentColor" stroke-width="1.5"/><path d="M5 4.5 8 7 5 9.5" fill="none" stroke="currentColor" stroke-width="1.5"/></svg></a></div>
  </div>
  <div class="arch-card" style="left:112px;top:429px">
    <div class="arch-date"><b>21</b><i>Feb</i></div>
    <div class="arch-body"><h4>At vero eos et accusamus et iusto odio issimos ducimus qui</h4><p>It is a long established fact tha a rea will be distracted readable</p><a>Read More <svg width="14" height="14" viewBox="0 0 14 14"><circle cx="7" cy="7" r="6" fill="none" stroke="currentColor" stroke-width="1.5"/><path d="M5 4.5 8 7 5 9.5" fill="none" stroke="currentColor" stroke-width="1.5"/></svg></a></div>
  </div>
  <div class="arch-card" style="left:614px;top:429px">
    <div class="arch-date"><b>21</b><i>Feb</i></div>
    <div class="arch-body"><h4>At vero eos et accusamus et iusto odio issimos ducimus qui</h4><p>It is a long established fact tha a rea will be distracted readable</p><a>Read More <svg width="14" height="14" viewBox="0 0 14 14"><circle cx="7" cy="7" r="6" fill="none" stroke="currentColor" stroke-width="1.5"/><path d="M5 4.5 8 7 5 9.5" fill="none" stroke="currentColor" stroke-width="1.5"/></svg></a></div>
  </div>
</section>

<section class="call">
  <div class="call-kicker">Call Us Today</div>
  <div class="call-phone">123-456-7890</div>
  <p class="call-copy">Lorem ipsum dolor sit amet, consectetur adipiscing elit, sed do eiusmod tempor incididunt ut labore et dolore magna aliqua. Ut enim ad minim veniam, quis nostrud exercitation</p>
  <div class="btn-solid" style="left:495px;top:299px;width:210px;height:56px">Request A Quote</div>
</section>

<footer class="site-footer">
  <div class="foot-brand"><span class="brand-dot"></span><span class="brand-name">The Pantry Compass</span></div>
  <div class="foot-head" style="left:479px">MENU</div>
  <ul class="foot-links"><li>HOME</li><li>BLOG</li><li>ARCHIVE</li><li>ABOUT ME</li><li>CONTACT ME</li></ul>
  <div class="foot-head" style="left:681px">CONTACT</div>
  <div class="contact-row" style="left:681px;top:110px">
    <span class="ico"><svg width="12" height="14" viewBox="0 0 12 14"><path d="M6 0a5 5 0 0 0-5 5c0 4 5 9 5 9s5-5 5-9a5 5 0 0 0-5-5z" fill="#1c1e26"/><circle cx="6" cy="5" r="1.8" fill="#fff"/></svg></span>
    <span>1458 Dummy Text<br>lorem, CA 91710</span>
  </div>
  <div class="contact-row" style="left:681px;top:164px">
    <span class="ico"><svg width="14" height="10" viewBox="0 0 14 10"><rect x="0.5" y="0.5" width="13" height="9" fill="none" stroke="#1c1e26"/><path d="M0.5 0.5 7 6l6.5-5.5" fill="none" stroke="#1c1e26"/></svg></span>
    <span>E mail Us<br>hello@pantrycompass.net</span>
  </div>
  <div class="foot-head" style="left:928px">FOLLOW US</div>
  <div class="follow-row" style="left:928px;top:110px"><span class="ico"></span><span>Like us on<br>CIRCLEFEED</span></div>
  <div class="follow-row" style="left:928px;top:164px"><span class="ico"></span><span>Follow us on<br>CHIRPLINE</span></div>
  <div class="follow-row" style="left:928px;top:218px"><span class="ico"></span><span>Follow us on<br>WORKNETLY</span></div>
  <div class="foot-rule"></div>
  <div class="copyright">Copyright © 2021 All Rights Reserved</div>
</footer>

</div>
</body>
</html>
```